Retirement maintenance and reinstatment brochure

We are looking for a capability statement/brochure outlining our skills and capabilities for maintenance, reinstatement and refurbishment work specific to the requirements of retirement villages in Australia

We are a new company, however our people have significant experience working in this industry

Target Market(s)

Retirement living facilities, aged care facilities, hospitals

Industry/Entity Type

Building

Colors

Designer to choose colors to be used in the design.

Requirements
Must have
• Not alot of wording. Stock images of building refurbishment to retirement living and aged care (carpenters, painters etc)
Nice to have
• 1-2 pages only
Should not have
• alot of meaningless writing

```html
<!DOCTYPE html>
<html lang="en">
<head>
<meta charset="utf-8">
<title>Harbourline Maintenance Group – Brochure</title>
<link rel="stylesheet" href="https://fonts.googleapis.com/css2?family=Montserrat:wght@300;400;500;600;700;800&display=swap">
<style>
  :root{
    --red:#c8202f;
    --red-deep:#a8172a;
    --navy:#1f3a7a;
    --blue:#3d6fc4;
    --paper:#f4f5f8;
    --paper-shade:#e3e6ee;
    --ink:#2b2f3a;
    --white:#ffffff;
    --stage:#d9dbe0;
  }
  *{box-sizing:border-box;margin:0;padding:0}
  html,body{width:1200px;height:789px;overflow:hidden;background:var(--stage);font-family:"Montserrat",sans-serif}
  .spread{position:absolute;left:77px;top:24px;width:1046px;height:740px;display:flex;box-shadow:0 6px 24px rgba(0,0,0,.18)}
  .page{position:relative;width:523px;height:740px;overflow:hidden;background:linear-gradient(160deg,var(--white),var(--paper) 55%,var(--paper-shade))}
  .page svg.shape{position:absolute;left:0;top:0;width:523px;height:740px}
  .photo{position:absolute;border-radius:50%;border:6px solid var(--blue);overflow:hidden}

  /* back page */
  .why{position:absolute;left:44px;top:62px;width:420px}
  .why h2{font-size:24px;font-weight:400;color:var(--navy);letter-spacing:.5px}
  .why h2 b{color:var(--red);font-weight:700}
  .why .rule{width:150px;height:2px;background:var(--blue);margin:6px 0 12px}
  .why p{font-size:9.5px;line-height:1.45;color:var(--ink)}
  .promise{position:absolute;left:44px;top:200px;width:420px;font-weight:800;font-size:17px;line-height:1.35;text-transform:uppercase;color:var(--navy)}
  .promise .hot{color:var(--red)}
  .promise .big{color:var(--red);font-size:21px;display:block}
  .photo-carpenter{left:60px;top:395px;width:180px;height:180px;background:radial-gradient(circle at 50% 40%,#b08a63,#5a4634 75%)}
  .photo-plaster{left:218px;top:410px;width:150px;height:150px;background:radial-gradient(circle at 60% 45%,#cfc4b8,#8f8578 80%)}
  .contact{position:absolute;left:44px;top:600px;color:var(--white)}
  .contact .label{font-size:15px;font-weight:500;letter-spacing:.5px}
  .contact .phone{font-size:24px;font-weight:700;display:flex;align-items:center;gap:8px;margin-bottom:10px}
  .contact .row{display:flex;align-items:flex-start;gap:10px;font-size:14px;line-height:1.3;margin-bottom:8px}
  .contact svg{flex:none;margin-top:2px}
  .licence{position:absolute;left:280px;top:610px;width:210px;color:var(--white);font-size:12px;line-height:1.4;text-align:center}
  .licence b{font-weight:800;text-transform:uppercase}

  /* front page */
  .brand{position:absolute;left:0;top:44px;width:523px;display:flex;justify-content:center;align-items:center;gap:12px}
  .brand .dot{width:40px;height:40px;border-radius:50%;background:var(--navy)}
  .brand .name{font-size:22px;font-weight:700;color:var(--navy);line-height:1.05;letter-spacing:.3px}
  .photo-painter{position:absolute;left:105px;top:112px;width:330px;height:380px;background:linear-gradient(180deg,#eef0f4 0%,#dcdfe6 55%,#c9ccd4 100%);border-radius:6px}
  .photo-engineer{left:360px;top:355px;width:140px;height:140px;background:radial-gradient(circle at 50% 40%,#9cc3ea,#3f6aa8 80%)}
  .about{position:absolute;left:40px;top:555px;color:var(--white)}
  .about h1{font-size:42px;font-weight:800;letter-spacing:.5px;line-height:1}
  .about .line1{font-size:14px;font-weight:700;text-transform:uppercase;margin-top:8px}
  .about .line2{font-size:12.5px;font-weight:400;text-transform:uppercase;margin-top:4px;letter-spacing:.2px}
  .about .rule{width:210px;height:4px;background:var(--blue);margin-top:8px}
</style>
</head>
<body>
<main class="spread">

  <section class="page page-back">
    <svg class="shape" viewBox="0 0 523 740" aria-hidden="true">
      <path d="M0,480 Q270,545 523,380 L523,740 L0,740Z" fill="var(--red)"/>
      <path d="M200,515 Q380,500 523,392" fill="none" stroke="var(--navy)" stroke-width="12"/>
    </svg>

    <div class="why">
      <h2>WHY <b>US?</b></h2>
      <div class="rule"></div>
      <p>Lorem ipsum dolor sit amet, consectetur adipiscing elit, sed do eiusmod tempor incididunt ut labore et dolore magna aliqua. Ut enim ad minim veniam, quis nostrud exercitation ullamco laboris nisi ut aliquip ex ea commodo consequat. Duis aute irure dolor in reprehenderit in voluptate velit esse cillum dolore eu fugiat nulla pariatur. Excepteur sint occaecat cupidatat non proident, sunt in culpa qui officia deserunt mollit anim id est laborum.</p>
    </div>

    <p class="promise">We have the ability to react quickly and <span class="hot">complete works</span> with as little as <span class="big">24 hours notice.</span></p>

    <div class="photo photo-carpenter" role="img" aria-label="Smiling carpenter in tool apron in a workshop"></div>
    <div class="photo photo-plaster" role="img" aria-label="Gloved hand patching plaster on a wall"></div>

    <div class="contact">
      <div class="label">CALL US</div>
      <div class="phone">
        <svg width="20" height="20" viewBox="0 0 20 20" aria-hidden="true"><circle cx="10" cy="10" r="8.5" fill="none" stroke="#fff" stroke-width="1.6"/><path d="M7 5.5l1.5 2.5-1 1a6 6 0 0 0 3.5 3.5l1-1 2.5 1.5-1 2c-4 0-8-4-8-8z" fill="#fff"/></svg>
        0123 456 789
      </div>
      <div class="row">
        <svg width="14" height="18" viewBox="0 0 14 18" aria-hidden="true"><path d="M7 1a5 5 0 0 0-5 5c0 4 5 9 5 9s5-5 5-9a5 5 0 0 0-5-5z" fill="none" stroke="#fff" stroke-width="1.6"/><circle cx="7" cy="6" r="1.8" fill="#fff"/></svg>
        <span>Address Line 1<br>Address line 2</span>
      </div>
      <div class="row">
        <svg width="14" height="14" viewBox="0 0 14 14" aria-hidden="true"><circle cx="7" cy="7" r="6" fill="none" stroke="#fff" stroke-width="1.4"/><ellipse cx="7" cy="7" rx="2.6" ry="6" fill="none" stroke="#fff" stroke-width="1.2"/><path d="M1 7h12" stroke="#fff" stroke-width="1.2"/></svg>
        <span>www.yourweb.com</span>
      </div>
    </div>

    <p class="licence"><b>We are licensed and insured</b><br>and have a full workplace health and safety compliance system.</p>
  </section>

  <section class="page page-front">
    <svg class="shape" viewBox="0 0 523 740" aria-hidden="true">
      <path d="M0,525 Q280,520 523,330 L523,740 L0,740Z" fill="var(--red)"/>
      <path d="M0,505 Q280,500 523,315" fill="none" stroke="var(--navy)" stroke-width="12"/>
    </svg>

    <div class="brand">
      <span class="dot"></span>
      <span class="name">HARBOURLINE<br>MAINTENANCE GROUP</span>
    </div>

    <div class="photo-painter" role="img" aria-label="Smiling painter in cap and white overalls holding a paint roller and brush"></div>
    <div class="photo photo-engineer" role="img" aria-label="Site supervisor in hard hat writing on a clipboard"></div>

    <div class="about">
      <h1>WE ARE A</h1>
      <p class="line1">Commercial building and maintenance company</p>
      <p class="line2">Established and located on the Sunshine Coast in QLD.</p>
      <div class="rule"></div>
    </div>
  </section>

</main>
</body>
</html>
```